New Managed IT company needs a business card

We are an IT management and support company that needs a business card design. I have a logo that I'll provide. Blues and blacks match the logo, but i'm open to anything. I want the card to help people take us seriously, but still have some energy and fun in it. The card should communicate stability and a solid company.

Target Market(s)

Target market includes Owners and Presidents at small businesses of 20 - 100 employees in the Pittsburgh PA area.

Industry/Entity Type

Information Technology

Contact Information for Business Card

i am open to other designs, but i imagine having only the logo on one side and then the logo plus all contact details on the other side.

Requirements
Must have
• Our logo
• Company name is optional if the logo makes it obvious
• A name - Cole Perrin
• A title - President
• A phone number - 724-XXX-XXXX
• A mobile phone number - 724-615-2748
• An email address - cperrin@techvaultgrid.com
• a website - techvaultgrid.com or www.techvaultgrid.com
Nice to have
• some people tell me the logo feels like a superhero theme, some fun with that idea might be good. I'm open to ideas.
Should not have
• stock photos of people or computers - especially old looking stuff.

```html
<!DOCTYPE html>
<html lang="en">
<head>
<meta charset="UTF-8">
<title>TechVault Grid – Business Card</title>
<link href="https://fonts.googleapis.com/css2?family=Exo+2:wght@400;600;700&display=swap" rel="stylesheet">
<style>
  :root {
    --backdrop: #d7d9dc;
    --frost-top: #f1f3f5;
    --frost-bottom: #dfe3e7;
    --ink: #0d0e10;
    --ink-soft: #1c1e22;
    --blue: #1f5cc6;
    --blue-deep: #0f3a8c;
    --silver: #c8ccd2;
    --logo-ink: #2a2c30;
    --name-blue: #1d4fb0;
    --title-grey: #d4d4d4;
    --detail: #c9c2b6;
    --icon: #2a5fb8;
  }
  * { box-sizing: border-box; margin: 0; padding: 0; }
  html, body {
    width: 1200px; height: 969px; overflow: hidden;
    background: var(--backdrop);
    font-family: "Exo 2", "Trebuchet MS", sans-serif;
  }
  .card {
    position: absolute; left: 100px; top: 200px;
    width: 1000px; height: 568px;
    border-radius: 6px; overflow: hidden;
    box-shadow: 0 14px 40px rgba(0,0,0,0.25);
  }
  .card-art { position: absolute; inset: 0; }
  .brand {
    position: absolute; left: 78px; top: 64px;
    display: flex; flex-direction: column; align-items: center;
  }
  .brand-dot {
    width: 114px; height: 114px; border-radius: 50%;
    background: var(--blue);
  }
  .brand-name {
    margin-top: 18px;
    font-weight: 700; font-size: 40px; letter-spacing: 4px;
    color: var(--logo-ink); text-align: center; line-height: 1.1;
  }
  .contact {
    position: absolute; right: 48px; top: 290px;
    text-align: right;
  }
  .person-name {
    font-weight: 600; font-size: 34px; letter-spacing: 1px;
    color: var(--name-blue); text-transform: uppercase;
    margin-right: 46px;
  }
  .person-title {
    font-size: 25px; letter-spacing: 1.5px; color: var(--title-grey);
    margin-right: 46px; margin-top: 2px;
  }
  .details { list-style: none; margin-top: 22px; }
  .details li {
    display: flex; justify-content: flex-end; align-items: center;
    gap: 18px; height: 38px;
    font-size: 23px; letter-spacing: 0.5px; color: var(--detail);
  }
  .details svg { width: 28px; height: 28px; flex: none; }
</style>
</head>
<body>
  <div class="card">
    <svg class="card-art" viewBox="0 0 1000 568" preserveAspectRatio="none">
      <defs>
        <linearGradient id="frost" x1="0" y1="0" x2="0" y2="1">
          <stop offset="0" stop-color="var(--frost-top)"/>
          <stop offset="1" stop-color="var(--frost-bottom)"/>
        </linearGradient>
        <linearGradient id="band" x1="0" y1="1" x2="1" y2="0">
          <stop offset="0" stop-color="var(--blue-deep)"/>
          <stop offset="0.5" stop-color="var(--blue)"/>
          <stop offset="1" stop-color="var(--blue-deep)"/>
        </linearGradient>
      </defs>
      <rect class="frost-field" width="1000" height="568" fill="url(#frost)"/>
      <polygon class="dark-field" points="0,385 206,530 1000,76 1000,568 0,568" fill="var(--ink)"/>
      <polygon class="silver-edge" points="0,380 206,525 1000,71 1000,78 206,532 0,387" fill="var(--silver)"/>
      <polygon class="blue-band" points="0,350 206,497 1000,40 1000,72 206,525 0,380" fill="url(#band)"/>
    </svg>

    <div class="brand">
      <div class="brand-dot"></div>
      <div class="brand-name">TECHVAULT<br>GRID</div>
    </div>

    <div class="contact">
      <div class="person-name">Cole Perrin</div>
      <div class="person-title">PRESIDENT</div>
      <ul class="details">
        <li>724-390-1164
          <svg viewBox="0 0 24 24"><path fill="var(--icon)" d="M6.6 10.8a15.1 15.1 0 0 0 6.6 6.6l2.2-2.2c.3-.3.7-.4 1-.2 1.1.4 2.3.6 3.6.6.6 0 1 .4 1 1V20c0 .6-.4 1-1 1A17 17 0 0 1 3 4c0-.6.4-1 1-1h3.5c.6 0 1 .4 1 1 0 1.3.2 2.5.6 3.6.1.3 0 .7-.2 1z"/></svg>
        </li>
        <li>724-615-2748
          <svg viewBox="0 0 24 24"><rect x="6.5" y="2" width="11" height="20" rx="2" fill="none" stroke="var(--icon)" stroke-width="1.8"/><circle cx="12" cy="18.5" r="1" fill="var(--icon)"/></svg>
        </li>
        <li>cperrin@techvaultgrid.com
          <svg viewBox="0 0 24 24"><rect x="3" y="6" width="18" height="13" rx="1" fill="var(--icon)"/><path d="M3 7l9 6 9-6" fill="none" stroke="var(--ink)" stroke-width="1.5"/></svg>
        </li>
        <li>www.techvaultgrid.com
          <svg viewBox="0 0 24 24"><circle cx="12" cy="12" r="9" fill="var(--icon)"/><path d="M3 12h18M12 3c3 3 3 15 0 18M12 3c-3 3-3 15 0 18" fill="none" stroke="var(--ink)" stroke-width="1.3"/></svg>
        </li>
      </ul>
    </div>
  </div>
</body>
</html>
```